Business Card Design

Electronic Security Installation Specialists

Check out our website at www.bramblecoastllc.com to see what we do.

Industry/Entity Type

Business

Contact Information for Business Card

Fern Ridge
Marisol Penton
318 Calloway Drive
Shepherdstow, WV 25443

Colors
3176b5
0455a3
ffffff

```html
<!DOCTYPE html>
<html lang="en">
<head>
<meta charset="utf-8">
<title>Fern Ridge Business Card</title>
<link rel="stylesheet" href="https://fonts.googleapis.com/css2?family=Open+Sans:wght@400;600;700&family=Oxanium:wght@700&display=swap">
<style>
  :root {
    --blue-bright: #3176b5;
    --blue-deep: #0455a3;
    --navy: #1f3f86;
    --navy-dark: #16306c;
    --white: #ffffff;
    --sky-light: #a9c6e6;
    --page: #e9eaec;
    --chevron: #c9d3e6;
  }
  * { box-sizing: border-box; margin: 0; padding: 0; }
  html, body { width: 1200px; height: 1200px; overflow: hidden; }
  body {
    background: var(--page);
    font-family: "Open Sans", Arial, sans-serif;
    position: relative;
  }
  .card {
    position: absolute;
    left: 108px;
    width: 958px;
    overflow: hidden;
    color: var(--white);
    box-shadow: 0 4px 14px rgba(0,0,0,0.25);
  }
  .card-front {
    top: 17px;
    height: 559px;
    background: radial-gradient(ellipse at 40% 45%, var(--blue-bright) 0%, var(--blue-deep) 45%, var(--navy-dark) 100%);
  }
  .card-back {
    top: 610px;
    height: 562px;
    background: var(--white);
  }
  .logo-panel {
    position: absolute;
    left: 48px; top: 41px;
    width: 480px; height: 104px;
    background: var(--white);
    border-radius: 22px;
    display: flex; align-items: center;
    padding-left: 26px;
    gap: 22px;
  }
  .logo-dot {
    width: 80px; height: 80px;
    border-radius: 50%;
    background: var(--navy);
    flex: none;
  }
  .logo-name {
    font-family: "Open Sans", Arial, sans-serif;
    font-weight: 600;
    font-size: 56px;
    letter-spacing: -1px;
    color: var(--navy);
    white-space: nowrap;
  }
  .tagline {
    position: absolute;
    left: 560px; top: 56px;
    width: 380px;
    text-align: center;
    font-family: "Oxanium", sans-serif;
    font-weight: 700;
    font-size: 29px;
    line-height: 44px;
    text-transform: uppercase;
  }
  .photo-cameras {
    position: absolute;
    left: 468px; top: 165px;
    width: 490px; height: 328px;
    background: linear-gradient(160deg, rgba(240,242,246,0.85) 0%, rgba(200,208,220,0.7) 50%, rgba(120,150,190,0.35) 100%);
  }
  .service-area {
    position: absolute;
    left: 48px; top: 316px;
    font-size: 23px;
    line-height: 34px;
  }
  .phone {
    position: absolute;
    left: 46px; top: 404px;
    display: flex; align-items: center; gap: 10px;
    font-weight: 700; font-style: italic;
    font-size: 38px;
  }
  .footer-band {
    position: absolute;
    left: 0; right: 0;
    height: 48px;
    background: linear-gradient(180deg, #2f4c97 0%, var(--navy) 60%, var(--navy-dark) 100%);
    border-top: 3px solid var(--white);
    display: flex; align-items: center; justify-content: center;
    font-weight: 700;
    font-size: 24px;
  }
  .card-front .footer-band { top: 492px; }
  .front-strip {
    position: absolute; left: 0; right: 0; top: 543px; height: 16px;
    background: linear-gradient(90deg, var(--sky-light), #dfe9f5);
  }
  .back-logo {
    position: absolute;
    left: 42px; top: 38px;
    display: flex; align-items: center; gap: 20px;
  }
  .back-logo .logo-dot { width: 102px; height: 102px; }
  .back-logo .logo-name { font-size: 72px; }
  .social-badge {
    position: absolute;
    left: 768px; top: 48px;
    width: 144px; height: 128px;
    border-radius: 20px;
    background: var(--navy);
    z-index: 2;
  }
  .social-badge::after {
    content: "";
    position: absolute;
    left: 16px; top: 14px; right: 16px; bottom: 16px;
    border-radius: 12px;
    background: linear-gradient(180deg, #5aa3d8, var(--blue-bright));
  }
  .back-panel {
    position: absolute;
    left: 0; right: 0; top: 173px; bottom: 0;
    background: radial-gradient(ellipse at 45% 35%, #3a5aae 0%, var(--navy) 60%, var(--navy-dark) 100%);
  }
  .services-title {
    position: absolute;
    left: 40px; top: 30px;
    font-weight: 700;
    font-size: 26px;
  }
  .services-list {
    position: absolute;
    list-style: none;
    top: 84px;
    font-size: 23px;
    line-height: 31px;
  }
  .services-list.col-a { left: 40px; }
  .services-list.col-b { left: 520px; }
  .services-list li::before {
    content: "\203A";
    color: var(--chevron);
    font-weight: 700;
    margin-right: 12px;
  }
  .contact-note {
    position: absolute;
    left: 0; right: 0; top: 236px;
    text-align: center;
    font-size: 23px;
    line-height: 32px;
  }
  .back-panel .footer-band { top: 322px; }
</style>
</head>
<body>

<section class="card card-front">
  <div class="logo-panel">
    <div class="logo-dot"></div>
    <span class="logo-name">FERN RIDGE</span>
  </div>
  <h1 class="tagline">Security Installation<br>Specialists</h1>
  <div class="photo-cameras" role="img" aria-label="Photo of security cameras mounted on a pole against the sky"></div>
  <p class="service-area">Martinsburg, Charles Town,<br>Frederick, Hagertown, and Cumberland</p>
  <p class="phone">
    <svg width="30" height="34" viewBox="0 0 24 24" aria-hidden="true"><path fill="#fff" d="M6.6 10.8c1.4 2.8 3.8 5.1 6.6 6.6l2.2-2.2c.3-.3.7-.4 1-.2 1.1.4 2.3.6 3.6.6.6 0 1 .4 1 1V20c0 .6-.4 1-1 1C10.6 21 3 13.4 3 4c0-.6.4-1 1-1h3.5c.6 0 1 .4 1 1 0 1.3.2 2.5.6 3.6.1.3 0 .7-.2 1z"/></svg>
    304-555-0187
  </p>
  <div class="footer-band">www.bramblecoastllc.com</div>
  <div class="front-strip"></div>
</section>

<section class="card card-back">
  <div class="back-logo">
    <div class="logo-dot"></div>
    <span class="logo-name">FERN RIDGE</span>
  </div>
  <div class="social-badge"></div>
  <div class="back-panel">
    <h2 class="services-title">Our Technical Services Include</h2>
    <ul class="services-list col-a">
      <li>Installation and Service</li>
      <li>Proposal Critique</li>
      <li>Installations Management</li>
      <li>Specification Documentation</li>
    </ul>
    <ul class="services-list col-b">
      <li>Maintenance</li>
      <li>Turnkey Systems</li>
      <li>Vantor LK200/X10 Certified</li>
      <li>Intrusion Detection</li>
    </ul>
    <p class="contact-note">To learn more about our security services for your site<br>please contact us . give us a call at 304-555-0187</p>
    <div class="footer-band">www.bramblecoastllc.com</div>
  </div>
</section>

</body>
</html>
```